Candle company needs a label for candle

Looking for a designer to create my candle label. I am going to attach a few pictures of my vision for the label as well as my Company Logo and jar I have puchased. I'm going for the modern rustic feel but you are the designer and have full trust in your abilities. The label is going to be printed on Kraft paper (2x3) so looking for the font to be black. The candle label MUST include the following information:
Wick Harbor Co.
NO. 01: Eucalyptus + Spearmint
Handmade In NJ
Soy Wax
9oz

Industry/Entity Type

Candle Industry

Colors

Designer to choose colors to be used in the design.

Requirements
Should not have
• Any images

```html
<!DOCTYPE html>
<html lang="en">
<head>
<meta charset="utf-8">
<title>Wick Harbor Co. — No. 01 Candle Label</title>
<link rel="stylesheet" href="https://fonts.googleapis.com/css2?family=Noto+Serif+Display:wght@300;400;500;600&display=swap">
<style>
  :root {
    --page: #ffffff;
    --kraft: #c9a17b;
    --kraft-light: #d0a982;
    --kraft-dark: #c19874;
    --ink: #0b0b0b;
  }
  * { margin: 0; padding: 0; box-sizing: border-box; }
  html, body {
    width: 1200px; height: 1200px; overflow: hidden;
    background: var(--page);
  }
  .canvas { position: relative; width: 1200px; height: 1200px; }
  .label {
    position: absolute; left: 323px; top: 185px; width: 554px; height: 831px;
    background:
      radial-gradient(circle at 30% 20%, var(--kraft-light), transparent 60%),
      radial-gradient(circle at 75% 80%, var(--kraft-dark), transparent 65%),
      var(--kraft);
  }
  .label-art { display: block; width: 554px; height: 831px; }
  .label-art text { font-family: "Noto Serif Display", serif; }
  .brand-block { fill: var(--ink); }
  .brand-name { fill: var(--kraft); font-weight: 300; }
  .number-mark { fill: var(--ink); font-weight: 500; }
  .detail { fill: var(--ink); font-weight: 400; }
  .weight { fill: var(--ink); font-weight: 600; }
  .rule { stroke: var(--ink); stroke-width: 1.5; }
</style>
</head>
<body>
<main class="canvas">
  <section class="label">
    <svg class="label-art" viewBox="0 0 554 831" xmlns="http://www.w3.org/2000/svg">
      <title>Wick Harbor Co. No. 01 Eucalyptus + Spearmint, Handmade In NJ, Soy Wax, 9oz</title>

      <g class="brand">
        <rect class="brand-block" x="60" y="60" width="434" height="306"/>
        <text class="brand-name" x="111" y="203" font-size="70" textLength="220" lengthAdjust="spacing">WICK</text>
        <text class="brand-name" x="111" y="274" font-size="70" textLength="332" lengthAdjust="spacing">HARBOR</text>
        <text class="brand-name" x="412" y="346" font-size="34" textLength="66" lengthAdjust="spacing">CO.</text>
      </g>

      <g class="number">
        <text class="number-mark" x="60" y="540" font-size="170" textLength="125" lengthAdjust="spacingAndGlyphs">NO.</text>
        <text class="number-mark" x="69" y="706" font-size="170" textLength="74" lengthAdjust="spacingAndGlyphs">01</text>
      </g>

      <g class="rules">
        <line class="rule" x1="200" y1="420" x2="200" y2="706"/>
        <line class="rule" x1="200" y1="555" x2="494" y2="555"/>
        <line class="rule" x1="200" y1="636" x2="494" y2="636"/>
      </g>

      <g class="details">
        <text class="detail" x="231" y="467" font-size="52" textLength="185" lengthAdjust="spacingAndGlyphs">Eucalyptus</text>
        <text class="detail" x="230" y="526" font-size="52" textLength="198" lengthAdjust="spacingAndGlyphs"><tspan font-size="30">+</tspan> Spearmint</text>
        <text class="detail" x="231" y="614" font-size="52" textLength="263" lengthAdjust="spacingAndGlyphs">Handmade In NJ</text>
        <text class="detail" x="231" y="697" font-size="52" textLength="137" lengthAdjust="spacingAndGlyphs">Soy Wax</text>
        <text class="weight" x="249" y="784" font-size="44" textLength="56" lengthAdjust="spacingAndGlyphs">9oz</text>
      </g>
    </svg>
  </section>
</main>
</body>
</html>
```